Veridian Token Bourse (front page)

We need a design of a front page for our Veridian Token Bourse website (vtbex.co.uk). Our company is based in the United Kingdom and offers investors from all over the world an opportunity to invest into bitcoin and litecoin.

We have been developing this cutting edge technology for past 2 years based on our in depth knowledge on conventional stock and currency trading technology and methodology. We have run many test against penetration, security and stability and now are ready to deploy.

Recent news about vulnerability of such platforms leave a great deal of unease from retail investors about investing into cryptocurrency. We are set to challenge this attitude. Our background is payments in particular regulated environment in the UK. We are keen to apply our wealth of experience to provide secure and reliable trading platform and advance cryptocurrency as means of legal tender.

The front page should be based on the feel and look of our current technology vtbex.co.uk. Some of you have already been involved in logo design for our company, please see the attached mockups. The page should have this minimalist design, very clean and light.

Seek inspiration form www.coinharbor.net, www.tradelumo.com, vip.quorzen.com and other bitcoin exchanges.

We look forward to receiving your ideas.

You can also refer to our social pages:
https://www.facebook.com/vtbex.co.uk
https://twitter.com/vtbex_uk

We would like you to focus your efforts at designing the page in such a way so that it is very easy for visitor be open an account with the exchange. We must focus at informing the visitor about the bitcoin, how to my buy, how to sell, look at the general overview of the maker and CONVERTING him/her sing up. This is the most important!!

Regards,
Tobin
Updates

Project Deadline Extended
Reason: Dear all, We are very keen on getting this design done right the first time. The key success is conversion of visitors to subscribers and then to traders. It is absolutely essential make the registration process as streamlined as possible! When we are calling them to act by "Change the world one bitcoin at a time" we should give them a opportunity to provide us with relevant account creation details: email, password, confirm password. Please visit remitfold.co.uk for ideas. Secondly, tell them what is a bitcoin, why a bitcoin is a good investment and how to invest. Finally, it is important to inform visitors of "who we are", what sets us apart from other exchanges, tell them about our experience. In our view graphs and live order books are important but they might turn some visitors away especially the ones that are not accustomed to online trading. Think of what would you like to see on the page if you wanted YOURSELF to invest. What would make you to create an account and use it? Think what will work, we are here to revolutionise how people do business.... any wild ideas put them to us. OUR BUDGET JUST GONE UP!!!

Target Market(s)

A combination of professional and consumer bitcoin investors.

Industry/Entity Type

Environment

Requirements
Must have
• News section

```html
<!DOCTYPE html>
<html lang="en">
<head>
<meta charset="utf-8">
<title>Veridian Token Bourse</title>
<link href="https://fonts.googleapis.com/css2?family=Raleway:wght@300;400;500;600;700&family=Open+Sans:wght@400;600;700&display=swap" rel="stylesheet">
<style>
:root{
  --dark:#3d3e42;
  --blue:#2aa3dd;
  --sky:#1fa9df;
  --chart:#55ade0;
  --orange:#ec6645;
  --yellow:#f5b90c;
  --paper:#f5f3ef;
  --row:#eef6fb;
  --line:#d9d9d9;
  --text:#555;
  --ink:#222;
}
*{margin:0;padding:0;box-sizing:border-box}
html,body{width:1200px;height:3163px;overflow:hidden}
body{font-family:"Open Sans",Arial,sans-serif;color:var(--text);background:#fff;position:relative}
.abs{position:absolute}
h1,h2,h3{font-family:"Raleway",Arial,sans-serif;font-weight:300;color:var(--ink)}

/* ticker */
.ticker{top:0;left:0;width:1200px;height:65px;background:var(--dark);display:flex}
.ticker-cell{flex:1;display:flex;align-items:center;justify-content:center;gap:12px;color:#fff;border-right:1px solid #555;font-size:14px;line-height:1.15}
.ticker-cell:last-child{border:0}
.ticker-cell b{font-weight:600;display:block;font-size:15px}
.ticker-cell span{color:#ccc}
.ticker-icon{width:26px;height:26px;border:2px solid #fff;border-radius:50%}

/* header */
.header{top:65px;left:0;width:1200px;height:112px}
.brand{left:108px;top:38px;display:flex;align-items:center;gap:10px;font-family:"Raleway",sans-serif;font-size:18px;font-weight:500;color:var(--dark);letter-spacing:1px}
.brand-dot{width:22px;height:22px;border-radius:50%;background:var(--blue)}
.login{left:603px;top:46px;display:flex;gap:7px;align-items:center}
.field{height:30px;border:1px solid var(--line);border-radius:15px;padding-left:24px;font-size:12px;color:#999;display:flex;align-items:center}
.login-go{width:38px;height:30px;border-radius:0 15px 15px 0;background:var(--blue);display:flex;align-items:center;justify-content:center}
.lang{margin-left:14px;width:48px;height:30px;border:1px solid var(--line);border-radius:15px;display:flex;align-items:center;gap:6px;padding-left:8px}
.lang i{width:18px;height:18px;border-radius:50%;background:#c9d3e6}

/* hero */
.hero{top:177px;left:0;width:1200px;height:481px;background:radial-gradient(circle at 75% 45%,#46c2ee,#139fd8 70%);overflow:hidden}
.hero h1{position:absolute;left:105px;top:128px;color:#fff;font-size:45px;font-weight:400;line-height:67px}
.btn-ghost{position:absolute;left:108px;top:283px;width:164px;height:42px;border:2px solid #fff;border-radius:21px;color:#fff;font-family:"Raleway",sans-serif;font-weight:700;font-size:16px;display:flex;align-items:center;justify-content:center;gap:8px}
.hero-art{position:absolute;left:696px;top:96px;width:380px;height:360px;border-radius:50%;background:radial-gradient(circle,#9fd23e 0%,#2d7cb8 55%,rgba(31,169,223,0) 72%)}

/* who */
.who{top:658px;left:0;width:1200px;height:359px;text-align:center}
.who h2{position:absolute;width:100%;top:73px;font-size:46px}
.subline{position:absolute;top:130px;left:470px;width:260px;display:flex;align-items:center;gap:10px;font-size:13px;letter-spacing:1px;color:#444;justify-content:center}
.subline::before,.subline::after{content:"";flex:1;height:1px;background:#bbb}
.who p{position:absolute;left:200px;width:800px;top:170px;font-size:14px;line-height:23px;color:#666}
.btn-outline{position:absolute;left:535px;top:278px;width:125px;height:31px;border:2px solid #333;border-radius:16px;font-size:12px;font-weight:700;color:#333;display:flex;align-items:center;justify-content:center}

/* overview */
.overview{top:1017px;left:0;width:1200px;height:1265px;background:var(--paper)}
.overview h2{position:absolute;left:108px;top:60px;font-size:44px}
.overview h2 small{font-size:18px;color:#444}
.rule{position:absolute;left:108px;width:985px;height:2px;background:#ddd}
.chart-panel{position:absolute;left:108px;top:158px;width:985px;height:571px;background:#fff;box-shadow:0 0 4px rgba(0,0,0,.08)}
.tf{position:absolute;left:32px;top:33px;display:flex;border:1px solid var(--line)}
.tf span{width:61px;height:37px;font-size:13px;color:#333;display:flex;align-items:center;justify-content:center}
.tf .on{background:var(--yellow);color:#fff;position:relative}
.tf .on::after{content:"";position:absolute;bottom:-7px;left:24px;border:7px solid transparent;border-bottom:0;border-top-color:var(--yellow)}
.chart-tabs{position:absolute;left:0;bottom:0;width:985px;height:37px;display:flex}
.chart-tabs span{flex:1;background:var(--dark);color:#eee;font-size:13px;display:flex;align-items:center;justify-content:center;border-left:1px solid #555}
.chart-tabs .on{background:#fff;color:#333;font-weight:600;flex:.7}

.orders{position:absolute;left:108px;top:807px;width:985px}
.order-tabs{display:flex;gap:2px;height:34px}
.order-tabs span{width:185px;background:#e8e6e2;font-size:14px;display:flex;align-items:center;justify-content:center;color:#444}
.order-tabs .on{background:#fff;color:var(--blue);font-size:16px}
table{width:985px;border-collapse:collapse;font-size:12.5px;background:#fff}
th{height:59px;font-weight:700;color:#333}
td{height:35.5px;color:#444;text-align:center}
tr:nth-child(odd) td{background:var(--row)}
th:first-child,td:first-child{text-align:left;padding-left:32px}

/* trade */
.trade-bar{top:2282px;left:0;width:1200px;height:46px;display:flex;color:#fff;font-size:15px}
.trade-bar div{display:flex;align-items:center;gap:10px;padding-left:108px}
.trade-bar b{font-family:"Raleway",sans-serif;font-size:24px;font-weight:700}
.buy{width:599px;background:var(--blue)}
.sell{flex:1;background:var(--orange);padding-left:24px!important}
.trade-form{top:2328px;left:0;width:1200px;height:144px}
.inputs{position:absolute;left:108px;top:26px;display:flex;gap:8px}
.inputs span{width:323px;height:38px;border:1px solid var(--line);font-size:12px;color:#888;padding-left:20px;display:flex;align-items:center}
.totals{position:absolute;left:108px;top:84px;display:flex;align-items:center;font-size:14px;color:#333}
.totals .sum{line-height:20px;padding-right:16px}
.totals .sum b{display:block}
.totals .sum+.sum{border-left:1px solid #ccc;padding-left:16px;margin-right:50px}
.btn{width:152px;height:35px;color:#fff;font-size:15px;display:flex;align-items:center;justify-content:center;margin-right:6px}
.commission{border-left:1px solid #ccc;padding-left:16px;margin-left:24px;font-size:14px}

/* news */
.news{top:2472px;left:0;width:1200px;height:253px;background:var(--paper)}
.news h2{position:absolute;left:108px;top:50px;font-size:40px;font-weight:400}
.news-item{position:absolute;top:135px;width:330px;display:flex;gap:14px}
.date{width:50px;height:56px;background:#222;color:#fff;text-align:center;font-size:9px;line-height:11px;padding-top:3px}
.date b{display:block;font-size:26px;line-height:28px}
.news-item h3{font-family:"Open Sans",sans-serif;font-size:15px;font-weight:400;color:var(--blue)}
.news-item p{font-size:12.5px;line-height:16px;color:#333;width:250px}
.arrow{position:absolute;top:148px}

/* tagline + footer */
.tagline{top:2738px;left:300px;width:600px;height:80px;background:linear-gradient(90deg,#fff,#d3ebf8 50%,#fff)}
.footer{top:2830px;left:0;width:1200px;height:270px;border-top:1px solid #e6e6e6}
.footer h4{font-size:14px;color:#222;font-weight:600;letter-spacing:.5px;margin-bottom:10px}
.col{position:absolute;top:44px;font-size:12px;line-height:19px;color:#333}
.col p{width:380px;line-height:19px}
.col a{display:block;color:#333;text-decoration:none}
.social{display:flex;gap:5px;margin-top:4px}
.social i{width:24px;height:24px;border-radius:50%;background:#333}
.foot-brand{left:108px;top:224px;font-family:"Raleway",sans-serif;font-size:12px;color:var(--dark);display:flex;gap:6px;align-items:center}
.copy{top:3100px;left:0;width:1200px;height:63px;background:var(--paper);font-size:12px;color:#333;padding:26px 0 0 108px}
</style>
</head>
<body>

<div class="abs ticker">
  <div class="ticker-cell"><i class="ticker-icon"></i><div><b>Last price</b><span>581.669 USD</span></div></div>
  <div class="ticker-cell"><i class="ticker-icon"></i><div><b>Low price</b><span>570 USD</span></div></div>
  <div class="ticker-cell"><i class="ticker-icon"></i><div><b>High price</b><span>585.994 USD</span></div></div>
  <div class="ticker-cell"><i class="ticker-icon"></i><div><b>Volume</b><span>196.2 BTC</span></div></div>
</div>

<header class="abs header">
  <div class="abs brand"><i class="brand-dot"></i>Veridian Token Bourse</div>
  <div class="abs login">
    <span class="field" style="width:194px">Email</span>
    <span class="field" style="width:175px">Password</span>
    <span class="login-go"><svg width="18" height="12" viewBox="0 0 18 12"><path d="M1 6h15M11 1l5 5-5 5" stroke="#fff" stroke-width="2" fill="none"/></svg></span>
    <span class="lang"><i></i><svg width="8" height="5"><path d="M0 0h8L4 5z" fill="#666"/></svg></span>
  </div>
</header>

<section class="abs hero">
  <svg class="abs" style="left:0;top:0" width="1200" height="481" viewBox="0 0 1200 481">
    <path d="M0 481V360l120-40 110 30 120-60 120 50 110-40 100 20v161z" fill="#3fb6e6" opacity=".5"/>
    <polyline points="180,465 243,443 307,447 370,435 433,397 490,397 555,378 610,385 680,367 740,330 800,335 1060,360 1115,390 1170,403" fill="none" stroke="#fff" stroke-width="3"/>
    <g fill="#fff" stroke="#1fa9df" stroke-width="3">
      <circle cx="180" cy="465" r="8"/><circle cx="243" cy="443" r="8"/><circle cx="307" cy="447" r="8"/><circle cx="370" cy="435" r="8"/><circle cx="433" cy="397" r="8"/><circle cx="490" cy="397" r="8"/><circle cx="555" cy="378" r="8"/><circle cx="610" cy="385" r="8"/><circle cx="680" cy="367" r="8"/><circle cx="1115" cy="390" r="8"/><circle cx="1170" cy="403" r="8"/>
    </g>
  </svg>
  <h1>Change The World One<br>Bitcoin At a Time</h1>
  <div class="btn-ghost"><svg width="16" height="16" viewBox="0 0 16 16"><path d="M8 0l2.4 5 5.6.6-4.2 3.8 1.2 5.6L8 12.2 3 15l1.2-5.6L0 5.6 5.6 5z" fill="#fff"/></svg>ABOUT US</div>
  <div class="hero-art" role="img" aria-label="Illustration of a laptop with banknotes, coins and a cursor inside a dotted circle"></div>
</section>

<section class="abs who">
  <h2>Who We Are</h2>
  <div class="subline">VERIDIAN TOKEN BOURSE</div>
  <p>Lorem ipsum dolor sit amet, consectetuer adipiscing elit, sed diam nonummy nibh euismod tincidunt ut laoreet dolore magna aliquam erat volutpat. Ut wisi enim ad minim veniam, quis nostrud exerci tation ullamcorper suscipit lobortis nisl ut aliquip ex ea commodo consequat. Duis autem vel eum iriure dolor in hendrerit in vulputate velit esse molestie consequat, vel illum dolore eu feugiat nulla facilisis at vero eros et accumsan.</p>
  <div class="btn-outline">READ MORE</div>
</section>

<section class="abs overview">
  <h2>Over View / <small>(BT/USD)</small></h2>
  <div class="rule" style="top:153px"></div>
  <div class="chart-panel">
    <div class="tf"><span>M1</span><span>M5</span><span class="on">M15</span><span>M30</span><span>H1</span><span>H4</span></div>
    <svg class="abs" style="left:0;top:0" width="985" height="534" viewBox="0 0 985 534">
      <g stroke="#e6e6e6"><line x1="93" y1="133" x2="953" y2="133"/><line x1="93" y1="190" x2="953" y2="190"/><line x1="93" y1="247" x2="953" y2="247"/><line x1="93" y1="304" x2="953" y2="304"/><line x1="93" y1="361" x2="953" y2="361"/><line x1="93" y1="418" x2="953" y2="418"/></g>
      <g font-size="13" fill="#888" font-family="Open Sans,sans-serif">
        <text x="32" y="137">586.4</text><text x="32" y="194">58530c</text><text x="32" y="251">584.2</text><text x="32" y="308">586.4</text><text x="32" y="365">58530c</text><text x="32" y="422">584.2</text>
        <text x="238" y="505">17.20</text><text x="385" y="505">17.30</text><text x="530" y="505">17.40</text><text x="675" y="505">17.50</text><text x="820" y="505">18.00</text>
      </g>
      <path d="M93 396L135 375L188 361L230 386L251 340L283 348L314 375L346 354L399 302L441 287L483 264L525 280L567 228L609 259L652 207L694 217L736 175L789 196L863 150L953 127V470H93z" fill="var(--chart)"/>
      <polyline points="135,453 215,424 299,437 382,420 462,365 546,382 628,335 713,356 795,297 877,272" fill="none" stroke="#fff" stroke-width="3"/>
      <g fill="#fff" stroke="#555" stroke-width="2.5">
        <circle cx="135" cy="453" r="8"/><circle cx="215" cy="424" r="8"/><circle cx="299" cy="437" r="8"/><circle cx="382" cy="420" r="8"/><circle cx="462" cy="365" r="8"/><circle cx="546" cy="382" r="8"/><circle cx="628" cy="335" r="8"/><circle cx="713" cy="356" r="8"/><circle cx="795" cy="297" r="8"/><circle cx="877" cy="272" r="8"/>
      </g>
      <line x1="0" y1="470" x2="985" y2="470" stroke="#ddd"/>
    </svg>
    <div class="chart-tabs"><span class="on">QUOTES</span><span>CANDLES</span><span>DEPTH</span><span>VOLUME</span></div>
  </div>

  <div class="orders">
    <div class="order-tabs"><span class="on">Active orders</span><span>All Orders</span><span>Trade History</span></div>
    <table>
      <tr><th>Market</th><th>Time</th><th>Type</th><th>Volume (BTC)</th><th>Price</th><th>Total (USD)</th></tr>
      <tr><td>BTC/USD</td><td>26/3/2014 20:17:49</td><td>Buy</td><td>0.06134</td><td>584</td><td>35.8226</td></tr>
      <tr><td>BTC/USD</td><td>26/3/2014 20:17:49</td><td>Buy</td><td>0.06134</td><td>584</td><td>35.8226</td></tr>
      <tr><td>BTC/USD</td><td>26/3/2014 20:17:49</td><td>Buy</td><td>0.06134</td><td>584</td><td>35.8226</td></tr>
      <tr><td>BTC/USD</td><td>26/3/2014 20:17:49</td><td>Buy</td><td>0.06134</td><td>584</td><td>35.8226</td></tr>
      <tr><td>BTC/USD</td><td>26/3/2014 20:17:49</td><td>Buy</td><td>0.06134</td><td>584</td><td>35.8226</td></tr>
      <tr><td>BTC/USD</td><td>26/3/2014 20:17:49</td><td>Buy</td><td>0.06134</td><td>584</td><td>35.8226</td></tr>
      <tr><td>BTC/USD</td><td>26/3/2014 20:17:49</td><td>Buy</td><td>0.06134</td><td>584</td><td>35.8226</td></tr>
      <tr><td>BTC/USD</td><td>26/3/2014 20:17:49</td><td>Buy</td><td>0.06134</td><td>584</td><td>35.8226</td></tr>
      <tr><td>BTC/USD</td><td>26/3/2014 20:17:49</td><td>Buy</td><td>0.06134</td><td>584</td><td>35.8226</td></tr>
    </table>
  </div>
</section>

<div class="abs trade-bar">
  <div class="buy"><b>Buy Btc</b>&rarr; 585.00000 USD</div>
  <div class="sell"><b>Sell Btc</b>&rarr; 584.00000 USD</div>
</div>
<section class="abs trade-form">
  <div class="inputs"><span>Type</span><span>Volume BTC</span><span>Price Per BTC</span></div>
  <div class="totals">
    <div class="sum"><b>Total</b>Usd 0.0000</div>
    <div class="sum"><b>Free</b>Btc 0.0000</div>
    <span class="btn" style="background:var(--blue)">Buy Btc</span>
    <span class="btn" style="background:#c9c9c9">Cancel</span>
    <span class="commission">Commission For The Transaction Is 0.2%</span>
  </div>
</section>

<section class="abs news">
  <h2>Latest News</h2>
  <div class="rule" style="top:108px;height:1px"></div>
  <svg class="arrow" style="left:50px" width="18" height="26"><path d="M15 2L4 13l11 11" stroke="#333" stroke-width="4" fill="none"/></svg>
  <svg class="arrow" style="left:1135px" width="18" height="26"><path d="M3 2l11 11L3 24" stroke="#333" stroke-width="4" fill="none"/></svg>
  <div class="news-item" style="left:108px"><div class="date">July<b>30</b>2013</div><div><h3>Marion Welcomes You!</h3><p>Printing and typesetting industry. Lorem Ipsum has been the industry's standard dummy...</p></div></div>
  <div class="news-item" style="left:462px"><div class="date">July<b>30</b>2013</div><div><h3>Marion Welcomes You!</h3><p>Printing and typesetting industry. Lorem Ipsum has been the industry's standard dummy...</p></div></div>
  <div class="news-item" style="left:816px"><div class="date">July<b>30</b>2013</div><div><h3>Marion Welcomes You!</h3><p>Printing and typesetting industry. Lorem Ipsum has been the industry's standard dummy...</p></div></div>
</section>

<div class="abs tagline" role="img" aria-label="Hand lettered blue script: Change the world one bitcoin at a time"></div>

<footer class="abs footer">
  <div class="col" style="left:108px"><h4>RISK DISCLAIMER</h4><p>Lorem ipsum dolor sit amet, consectetuer adipiscing elit, sed diam nonummy nibh euismod tincidunt ut laoreet dolore magna aliquam erat volutpat. Ut wisi enim ad minim veniam, quis nostrud exerci tation ullamcorper suscipit lobortis nisl ut aliquip ex ea commodo consequat.</p><a style="margin-top:10px;font-weight:600">Read More</a></div>
  <div class="col" style="left:572px"><h4>ABOUT</h4><a>About us</a><a>News</a><a>Fee Schedule</a><a>Terms of Use</a><a>Privacy Policy</a><a>Cookie Statement</a></div>
  <div class="col" style="left:789px"><h4>DATA</h4><a>Overview</a><a>Order Book</a><a>API</a><div class="social"><i></i><i></i><i></i><i></i></div></div>
  <div class="col" style="left:964px"><h4>HELP</h4><a>What is Bitcoin?</a><a>How can I get Bitcoin?</a><a>Who uses Bitcoin?</a><a>Refund Policy</a><a>Fees</a><a>Partners</a></div>
  <div class="abs foot-brand"><i class="brand-dot" style="width:14px;height:14px"></i>Veridian Token Bourse</div>
</footer>

<div class="abs copy">Copyrights &copy; 2013 - 2014 VTB</div>

</body>
</html>
```